Residential Construction Business - Site Signage

I need a design made for a site fence banner. We have a logo and branding so the design would need to be aligned with this. It would need to be made to specific size ratio so that it can be sent to the maker for production.
ratio : 4600 wide x 1700 high
The design should feature our website and also the slogan
"don't move, re-imagine"

Target Market(s)

potential clients

Industry/Entity Type

construction

Font styles to use
Other font styles liked:
• to match branding

Colors
0054AA
0677BA
7BADD7
CADEEF
E8F1F8

Requirements
Must have
• www.velmbuild.com.au Majority of the sign is our brand logo
Nice to have
• Majority of the sign is our brand logo
Should not have
• colors and themes that arent brand relevant

```html
<!DOCTYPE html>
<html lang="en">
<head>
<meta charset="utf-8">
<title>Velm Build – Site Fence Banner</title>
<link rel="stylesheet" href="https://fonts.googleapis.com/css2?family=Outfit:wght@400;600&display=swap">
<style>
  :root {
    --navy: #063C5E;
    --brand-blue: #0054AA;
    --accent-blue: #0677BA;
    --white: #FFFFFF;
    --photo-top: #EEEDEC;
    --photo-mid: #F2F1F0;
    --photo-bottom: #D8C2A2;
  }
  html, body {
    margin: 0;
    padding: 0;
    width: 1200px;
    height: 976px;
    overflow: hidden;
    background: var(--white);
  }
  .canvas {
    position: relative;
    width: 1200px;
    height: 976px;
  }
  .banner {
    position: absolute;
    left: 48px;
    width: 1104px;
    height: 408px;
    display: block;
  }
  .banner--navy { top: 48px; }
  .banner--blue { top: 520px; }
  .brand-name {
    font-family: "Outfit", sans-serif;
    font-weight: 600;
    fill: var(--white);
    letter-spacing: 10px;
  }
  .slogan {
    font-family: "Outfit", sans-serif;
    font-weight: 600;
    font-size: 116px;
    fill: var(--white);
  }
  .web-address {
    font-family: "Outfit", sans-serif;
    font-weight: 400;
    font-size: 62px;
    fill: var(--white);
  }
  .panel--navy { fill: var(--navy); }
  .panel--blue { fill: var(--brand-blue); }
  .logo-block { fill: var(--navy); }
  .marker--accent { fill: var(--accent-blue); }
  .marker--white { fill: var(--white); }
</style>
</head>
<body>
<main class="canvas">

  <svg class="banner banner--navy" viewBox="0 0 1965 726" xmlns="http://www.w3.org/2000/svg">
    <defs>
      <linearGradient id="interior-tones-a" x1="0" y1="0" x2="0" y2="1">
        <stop offset="0" stop-color="var(--photo-top)"/>
        <stop offset="0.55" stop-color="var(--photo-mid)"/>
        <stop offset="1" stop-color="var(--photo-bottom)"/>
      </linearGradient>
    </defs>
    <rect class="interior-photo" role="img" aria-label="Faded photo of a bright renovated living room with sheer curtains, a tan sofa and a dining area" x="0" y="0" width="1965" height="726" fill="url(#interior-tones-a)"/>
    <path class="panel--navy" d="M918 0 H1965 V726 H891 L1200 417 Q1240 377 1200 327 Z"/>
    <path class="logo-block" d="M84 126 H715 L530 340 Q510 363 530 386 L733 603 H84 Z"/>
    <text class="brand-name" x="130" y="385" font-size="64" textLength="370" lengthAdjust="spacing">VELM BUILD</text>
    <text class="slogan" x="1880" y="337" text-anchor="end">Don't move</text>
    <text class="slogan" x="1880" y="447" text-anchor="end">Re-imagine</text>
    <text class="web-address" x="1878" y="640" text-anchor="end">www.velmbuild.com.au</text>
    <rect class="marker--accent" x="1920" y="600" width="45" height="50"/>
  </svg>

  <svg class="banner banner--blue" viewBox="0 0 1965 726" xmlns="http://www.w3.org/2000/svg">
    <defs>
      <linearGradient id="interior-tones-b" x1="0" y1="0" x2="0" y2="1">
        <stop offset="0" stop-color="var(--photo-top)"/>
        <stop offset="0.55" stop-color="var(--photo-mid)"/>
        <stop offset="1" stop-color="var(--photo-bottom)"/>
      </linearGradient>
    </defs>
    <rect class="interior-photo" role="img" aria-label="Faded photo of a bright renovated living room with sheer curtains, a tan sofa and a dining area" x="0" y="0" width="1965" height="726" fill="url(#interior-tones-b)"/>
    <path class="panel--blue" d="M918 0 H1965 V726 H891 L1200 417 Q1240 377 1200 327 Z"/>
    <path class="logo-block" d="M84 126 H715 L530 340 Q510 363 530 386 L733 603 H84 Z"/>
    <text class="brand-name" x="130" y="385" font-size="64" textLength="370" lengthAdjust="spacing">VELM BUILD</text>
    <text class="slogan" x="1880" y="337" text-anchor="end">Don't move</text>
    <text class="slogan" x="1880" y="447" text-anchor="end">Re-imagine</text>
    <text class="web-address" x="1878" y="640" text-anchor="end">www.velmbuild.com.au</text>
    <rect class="marker--white" x="1920" y="600" width="45" height="50"/>
  </svg>

</main>
</body>
</html>
```